Wordpress Website Update - Elementor

I'm currently using Elementor and would like my site to be updated. A nice facelift to the current pages. We are a small boutique animation service company.
I have a list of similar production houses to use as references and would like the format/style of the site not to feel so corporate and infuse the fun that we bring to working with clients on animated projects.

Additionally, I'd like to add 2 more pages focusing on more portfolio work and Original IP - which is now our primary goal to sell our show ideas. Maybe have a password projected behind an image showcasing the show/ film. Go to our current site to review. www.lumafrothstudio.com

Target Market(s)

Animation/ Commercials/ Vexora/ Tirzel/ Quonk/ ZVR - Okay with first page being shorter and not as long as well. Have contact us 'above the fold' on options as well.

Industry/Entity Type

Animation and Film

Coding

Coded - Design and coding required

Requirements
Must have
• Current 3 pages - additional 2 - we can focus on layout and arrangement with temporary images then swap with real assets when ready.
Nice to have
• site examples: quillpinestudios.com, Parsel House, Wembi Studios, Gorflet.net, Brightwell Animation, Lanternhook Animation Studios, ZeZo Studios use Orvane Max as inspiration.

```html
<!DOCTYPE html>
<html lang="en">
<head>
<meta charset="utf-8">
<title>Lumafroth Productions</title>
<link rel="stylesheet" href="https://fonts.googleapis.com/css2?family=Ubuntu:wght@500;700&family=Poppins:wght@500;600;700&family=Montserrat:wght@400;500;600&display=swap">
<style>
:root{
  --bg:#1e1d2e;
  --band:#24233a;
  --black:#000;
  --white:#ffffff;
  --grey:#c9c9d2;
  --purple:#6a33d6;
  --pink:#e81e50;
  --lilac:#9a80f0;
  --logo:#8a4ff0;
  --cta-bg:#eef3ec;
  --ink:#1e1d2e;
  --grad:linear-gradient(90deg,#d81a5c,#5a2bd0);
}
*{margin:0;padding:0;box-sizing:border-box}
html,body{width:1200px;height:2993px;overflow:hidden;background:var(--bg)}
body{position:relative;font-family:"Montserrat",sans-serif;color:var(--white)}
.abs{position:absolute}
.art{position:absolute}
/* header */
.site-header{position:absolute;left:0;top:0;width:1200px;height:93px;background:var(--bg)}
.nav-link{position:absolute;top:34px;font-family:"Poppins",sans-serif;font-weight:600;font-size:20px;color:var(--white);text-decoration:none}
.brand{position:absolute;font-family:"Ubuntu",sans-serif;font-weight:700;color:var(--logo);letter-spacing:1px;transform:translateX(-50%);white-space:nowrap}
.social{position:absolute;display:flex;gap:8px}
.social span{width:30px;height:30px;border:1.5px solid var(--grey);border-radius:50%;display:block}
/* hero */
.hero-band{position:absolute;left:0;top:93px;width:1200px;height:507px;background:var(--black)}
.arrow{position:absolute}
/* section headings */
.heading-band{position:absolute;background:var(--band)}
.section-title{position:absolute;font-family:"Ubuntu",sans-serif;font-weight:700;font-size:44px;color:var(--white);line-height:1}
.ip-card{position:absolute;width:242px;height:172px;border-radius:8px}
.ip-caption{position:absolute;font-size:16px;font-weight:500;letter-spacing:.3px}
/* features */
.feature-label{position:absolute;top:1372px;width:400px;height:135px;padding:24px 0 0 74px}
.feature-label h3{font-family:"Ubuntu",sans-serif;font-weight:700;font-size:30px;line-height:1;margin-bottom:12px;white-space:nowrap}
.feature-label p{font-size:16px;line-height:25px;width:270px}
/* projects */
.eyebrow{position:absolute;left:0;width:1200px;text-align:center;color:var(--pink);font-size:19px;font-weight:500}
.btn{position:absolute;display:flex;align-items:center;justify-content:center;border-radius:26px;background:var(--grad);font-family:"Poppins",sans-serif;font-weight:600;font-size:19px;color:var(--white);text-decoration:none}
.client{position:absolute;top:2372px;font-family:"Ubuntu",sans-serif;font-weight:700;font-size:28px;color:#b9b9c4;white-space:nowrap;display:flex;align-items:center;gap:8px}
.client i{display:block;width:20px;height:20px;border-radius:50%;background:#b9b9c4}
/* cta */
.cta{position:absolute;left:0;top:2556px;width:1200px;height:334px;background:var(--cta-bg)}
.cta h2{position:absolute;left:76px;top:86px;font-family:"Ubuntu",sans-serif;font-weight:700;font-size:46px;color:var(--ink);white-space:nowrap}
.cta p{position:absolute;left:75px;top:147px;font-size:20px;color:var(--ink)}
/* footer */
.site-footer{position:absolute;left:0;top:2890px;width:1200px;height:103px;background:var(--bg)}
.copyright{position:absolute;left:76px;top:43px;font-size:13px;color:var(--white)}
</style>
</head>
<body>

<header class="site-header">
  <a class="nav-link" style="left:74px" href="#">Home</a>
  <a class="nav-link" style="left:175px" href="#">About Us</a>
  <a class="nav-link" style="left:308px" href="#">Services</a>
  <div class="brand" style="left:600px;top:22px;font-size:38px">LUMAFROTH</div>
  <a class="nav-link" style="left:753px;top:31px" href="#">Projects</a>
  <a class="nav-link" style="left:877px;top:31px" href="#">Contact</a>
  <div class="social" style="left:985px;top:31px"><span></span><span></span><span></span><span></span></div>
</header>

<section class="hero-band">
  <div class="art" role="img" aria-label="Animated scene of a red brick house on a green lawn" style="left:0;top:73px;width:163px;height:360px;background:linear-gradient(180deg,#9ec4e0,#8aa070 70%,#cfd4c8)"></div>
  <div class="art" role="img" aria-label="Animated puppy character wearing a headset" style="left:163px;top:36px;width:239px;height:433px;background:linear-gradient(160deg,#7a3ad8,#3a1a66 60%,#b07070)"></div>
  <div class="art" role="img" aria-label="Two animated bears scuba diving among fish" style="left:402px;top:0;width:396px;height:507px;background:linear-gradient(180deg,#4fa8e8,#1d5fb8 60%,#163f86)"></div>
  <div class="art" role="img" aria-label="Animated giraffe wearing glasses" style="left:798px;top:36px;width:239px;height:433px;background:linear-gradient(180deg,#6b6f72,#8a6a44 60%,#4a4a48)"></div>
  <div class="art" role="img" aria-label="Animated girl playing a harmonica" style="left:1037px;top:73px;width:163px;height:360px;background:linear-gradient(180deg,#4a8aa0,#7a4a30 50%,#d24a5a)"></div>
  <div class="art" aria-hidden="true" style="left:402px;top:507px;width:396px;height:45px;background:linear-gradient(180deg,#163f86,rgba(30,29,46,0))"></div>
  <svg class="arrow" style="left:36px;top:326px" width="40" height="38" viewBox="0 0 40 38"><path d="M38 19H6M20 4L5 19l15 15" fill="none" stroke="#d9d9d9" stroke-width="5" stroke-linecap="round" stroke-linejoin="round"/></svg>
  <svg class="arrow" style="left:1140px;top:326px" width="40" height="38" viewBox="0 0 40 38"><path d="M2 19h32M20 4l15 15-15 15" fill="none" stroke="#d9d9d9" stroke-width="5" stroke-linecap="round" stroke-linejoin="round"/></svg>
</section>

<!-- original IP -->
<div class="heading-band" style="left:79px;top:695px;width:1048px;height:72px"></div>
<h2 class="section-title" style="left:85px;top:712px">Lumafroth Original IP</h2>
<svg class="arrow" style="left:1070px;top:722px" width="24" height="22" viewBox="0 0 24 22"><path d="M22 11H4M12 3L3 11l9 8" fill="none" stroke="#fff" stroke-width="3" stroke-linecap="round" stroke-linejoin="round"/></svg>
<svg class="arrow" style="left:1103px;top:722px" width="24" height="22" viewBox="0 0 24 22"><path d="M2 11h18M12 3l9 8-9 8" fill="none" stroke="#e81e50" stroke-width="3" stroke-linecap="round" stroke-linejoin="round"/></svg>

<div class="ip-card" role="img" aria-label="Elf character beside a festive slot machine" style="left:74px;top:802px;background:linear-gradient(135deg,#e8c890,#b8242a 60%,#6a8a3a)"></div>
<div class="ip-card" role="img" aria-label="Pencil storyboard of a city skyline with a robot" style="left:345px;top:802px;background:linear-gradient(180deg,#f2f2f2,#9a9a9a)"></div>
<div class="ip-card" role="img" aria-label="Fantasy cave with a ship and glowing crystals" style="left:615px;top:802px;background:linear-gradient(135deg,#2a2aa0,#6a40d0 55%,#1a1a5a)"></div>
<div class="ip-card" role="img" aria-label="Storyboard panels in black and white" style="left:885px;top:802px;background:linear-gradient(180deg,#d8d8d8,#3a3a3a)"></div>
<p class="ip-caption" style="left:73px;top:990px">Neque porro quisquam</p>
<p class="ip-caption" style="left:344px;top:990px">Neque porro quisquam</p>
<p class="ip-caption" style="left:613px;top:990px">Neque porro quisquam</p>
<p class="ip-caption" style="left:883px;top:990px">Neque porro quisquam</p>

<!-- features -->
<div class="art" role="img" aria-label="Animated sloth smiling" style="left:0;top:1090px;width:400px;height:282px;background:linear-gradient(135deg,#b8a888,#8a7a60 55%,#3a9a8a)"></div>
<div class="art" role="img" aria-label="Animated giraffes in a living room" style="left:400px;top:1090px;width:400px;height:282px;background:linear-gradient(180deg,#8a9098,#9a7a50 60%,#5a4a3a)"></div>
<div class="art" role="img" aria-label="Artist working at a computer in a studio" style="left:800px;top:1090px;width:400px;height:282px;background:linear-gradient(135deg,#3a4a70,#1a2040 60%,#2a6a8a)"></div>
<svg class="arrow" style="left:36px;top:1235px" width="40" height="38" viewBox="0 0 40 38"><path d="M38 19H6M20 4L5 19l15 15" fill="none" stroke="#d9d9d9" stroke-width="5" stroke-linecap="round" stroke-linejoin="round"/></svg>
<svg class="arrow" style="left:1140px;top:1235px" width="40" height="38" viewBox="0 0 40 38"><path d="M2 19h32M20 4l15 15-15 15" fill="none" stroke="#d9d9d9" stroke-width="5" stroke-linecap="round" stroke-linejoin="round"/></svg>
<div class="feature-label" style="left:0;background:var(--purple)"><h3>Animation Reel</h3><p>Story and Animation is where LFS thrives.</p></div>
<div class="feature-label" style="left:400px;background:var(--pink);padding-left:26px"><h3>Giraffes &amp; Kids Are Free!</h3><p>Fresh Out The Render Oven. Careful It's</p></div>
<div class="feature-label" style="left:800px;background:var(--lilac);padding-left:23px"><h3>Our Expertise</h3><p>Creative Experts That Solve Problems</p></div>

<!-- projects -->
<div class="heading-band" style="left:344px;top:1574px;width:513px;height:102px"></div>
<p class="eyebrow" style="top:1589px">Just A Few</p>
<h2 class="section-title" style="left:0;width:1200px;text-align:center;top:1620px">Our Projects</h2>
<div class="art" role="img" aria-label="Purple furry monster character" style="left:1020px;top:1510px;width:180px;height:302px;border-radius:90px 0 0 40px;background:linear-gradient(160deg,#b070f0,#7a50e0 60%,#5a3ac0)"></div>

<div class="art" role="img" aria-label="Blue robot character turnaround" style="left:0;top:1812px;width:206px;height:188px;background:linear-gradient(180deg,#0a0a0a,#3a8ad0 60%,#7ab8e8)"></div>
<div class="art" role="img" aria-label="Mascot characters at a city parade" style="left:216px;top:1712px;width:206px;height:188px;background:linear-gradient(180deg,#8ac0e0,#5a88b8 55%,#a88868)"></div>
<div class="art" role="img" aria-label="Bears scuba diving among fish" style="left:216px;top:1912px;width:206px;height:186px;background:linear-gradient(180deg,#4fa8e8,#1d5fb8)"></div>
<div class="art" role="img" aria-label="Animated giraffe wearing glasses" style="left:433px;top:1712px;width:333px;height:386px;background:linear-gradient(180deg,#6b6f72,#8a6a44 60%,#d8d8d8)"></div>
<div class="art" role="img" aria-label="Animated house on a green lawn" style="left:777px;top:1712px;width:207px;height:188px;background:linear-gradient(180deg,#9ec4e0,#7a9a5a 70%,#c8c8c0)"></div>
<div class="art" role="img" aria-label="Snowy forest scene with characters" style="left:777px;top:1912px;width:207px;height:186px;background:linear-gradient(135deg,#f0f0f0,#4a8a4a 55%,#c88a4a)"></div>
<div class="art" role="img" aria-label="Animated professor beside a presenter" style="left:994px;top:1812px;width:206px;height:188px;background:linear-gradient(90deg,#6a7a88,#b8b0a8 55%,#8a8a88)"></div>

<a class="btn" style="left:489px;top:2137px;width:221px;height:51px" href="#">View All Projects</a>

<!-- clients -->
<div class="heading-band" style="left:79px;top:2261px;width:1048px;height:72px"></div>
<h2 class="section-title" style="left:85px;top:2277px">Our Clients</h2>
<svg class="arrow" style="left:1070px;top:2287px" width="24" height="22" viewBox="0 0 24 22"><path d="M22 11H4M12 3L3 11l9 8" fill="none" stroke="#fff" stroke-width="3" stroke-linecap="round" stroke-linejoin="round"/></svg>
<svg class="arrow" style="left:1103px;top:2287px" width="24" height="22" viewBox="0 0 24 22"><path d="M2 11h18M12 3l9 8-9 8" fill="none" stroke="#e81e50" stroke-width="3" stroke-linecap="round" stroke-linejoin="round"/></svg>

<div class="client" style="left:74px">FERROVANE</div>
<div class="client" style="left:250px">cloudrise</div>
<div class="client" style="left:452px"><i></i>NUVRA</div>
<div class="client" style="left:614px">SKELBY</div>
<div class="client" style="left:776px"><i></i>Trackwell</div>
<div class="client" style="left:980px;font-size:20px">Learnfest Show</div>

<!-- call to action -->
<section class="cta">
  <h2>Why Wait Let's Co-Create!</h2>
  <p>No need to scroll, save your finger and drop us a line.</p>
  <a class="btn" style="left:77px;top:191px;width:179px;height:51px" href="#">Contact Us</a>
</section>
<div class="art" role="img" aria-label="Green one-eyed furry monster cheering" style="left:800px;top:2457px;width:350px;height:400px;border-radius:45% 45% 40% 40%;background:radial-gradient(circle at 50% 45%,#a8d860,#78b830 60%,#5a9a28)"></div>

<footer class="site-footer">
  <p class="copyright">Copyright © 2022 Lumafroth Productions. All rights reserved.</p>
  <div class="brand" style="left:600px;top:30px;font-size:32px">LUMAFROTH</div>
  <div class="social" style="left:985px;top:36px"><span></span><span></span><span></span><span></span></div>
</footer>

</body>
</html>
```